kestrel paving

hay i have like a template of the site id like an can we just make it so i can edit all pictures an txt a will

also can my domain be
kestrelpaving.com.au

is this even the right place for this ?

Target Market(s)

everyone

Industry/Entity Type

Domain

Requirements
Must have
• everytings ready to go i think

```html
<!DOCTYPE html>
<html lang="en">
<head>
<meta charset="utf-8">
<title>Kestrel Paving</title>
<link href="https://fonts.googleapis.com/css2?family=Raleway:wght@400;500;600&family=Open+Sans:wght@400;600&display=swap" rel="stylesheet">
<style>
  :root {
    --ink: #1c1c1c;
    --body: #5a5a5a;
    --tan: #8f7659;
    --tan-light: #bfae97;
    --tan-dark: #7e6b55;
    --nav-top: #c2b29c;
    --nav-bottom: #8c7a63;
    --band-light: #c4b5a0;
    --band-dark: #9c8a73;
    --peach: #f4c9a0;
    --footer: #1e1e1e;
    --white: #ffffff;
  }
  * { box-sizing: border-box; margin: 0; padding: 0; }
  html, body { width: 947px; height: 1200px; overflow: hidden; background: var(--white); }
  body { position: relative; font-family: "Open Sans", sans-serif; color: var(--body); }
  .abs { position: absolute; }

  .brand { left: 118px; top: 62px; display: flex; align-items: center; gap: 8px;
    font-family: "Raleway", sans-serif; font-weight: 600; font-size: 22px; color: var(--tan); letter-spacing: 0.5px; }
  .brand-mark { width: 14px; height: 14px; border-radius: 50%; background: var(--tan); }

  .quote { right: 114px; top: 58px; text-align: right; font-family: "Open Sans", sans-serif; }
  .quote-label { font-size: 11.5px; color: #555; letter-spacing: 0.3px; }
  .quote-phone { display: flex; align-items: center; justify-content: flex-end; gap: 4px; font-size: 19px; color: var(--ink); margin-top: 1px; }

  .nav { left: 114px; top: 104px; width: 720px; height: 38px; display: flex;
    background: linear-gradient(to bottom, var(--nav-top), var(--nav-bottom)); }
  .nav a { display: flex; align-items: center; justify-content: center; color: var(--white); text-decoration: none;
    font-family: "Raleway", sans-serif; font-weight: 500; font-size: 11.5px; border-right: 1px solid rgba(255,255,255,0.35); }
  .nav a.active { background: linear-gradient(to bottom, #6e5e4c, #9a8770); }

  .hero { left: 114px; top: 142px; width: 719px; height: 318px;
    background: linear-gradient(to bottom, #8a9099 0%, #b5b2a8 38%, #6d6a63 60%, #3f3c38 100%); }
  .hero-caption { left: 151px; top: 232px; width: 297px; height: 128px; background: rgba(20,20,20,0.72); padding: 22px 0 0 25px; }
  .hero-kicker { font-family: "Raleway", sans-serif; font-size: 14.5px; color: var(--white); }
  .hero-title { font-family: "Raleway", sans-serif; font-size: 29px; color: var(--peach); line-height: 1.15; }
  .hero-text { font-size: 8.5px; color: #9a9a9a; line-height: 1.5; margin-top: 4px; width: 255px; }
  .dots { left: 452px; top: 441px; display: flex; gap: 3px; }
  .dots span { width: 10px; height: 10px; border-radius: 50%; background: var(--white); border: 1px solid #999; }

  .intro { left: 150px; top: 488px; width: 647px; text-align: center; }
  .intro h1 { font-family: "Raleway", sans-serif; font-weight: 500; font-size: 22px; color: var(--ink); letter-spacing: 0.3px; }
  .intro h2 { font-family: "Raleway", sans-serif; font-weight: 500; font-size: 14px; color: var(--ink); margin-top: 8px; }
  .intro p { font-size: 8.2px; line-height: 1.65; margin-top: 9px; color: #777; }

  .service { width: 229px; }
  .service-photo { width: 229px; height: 109px; border: 1px solid #ccc; }
  .service h3 { font-family: "Raleway", sans-serif; font-weight: 600; font-size: 16px; color: var(--tan); margin: 8px 0 0 2px; }
  .service p { font-size: 8.2px; line-height: 1.65; margin: 4px 0 0 2px; color: #555; }
  .btn { display: inline-block; margin: 8px 0 0 3px; width: 72px; height: 21px; line-height: 21px; text-align: center;
    background: linear-gradient(to bottom, #3a3a3a, #151515); color: var(--white); font-size: 7.5px; font-weight: 600; border-radius: 2px; }

  .projects { left: 0; top: 874px; width: 947px; height: 246px;
    background: radial-gradient(ellipse at 50% 40%, var(--band-light) 0%, #b3a28b 60%, var(--band-dark) 100%); }
  .projects-title { left: 0; top: 900px; width: 947px; display: flex; align-items: center; justify-content: center; gap: 10px;
    font-family: "Raleway", sans-serif; font-weight: 500; font-size: 16px; color: var(--ink); }
  .projects-title::before, .projects-title::after { content: ""; width: 270px; height: 1px; background: rgba(70,55,40,0.35); }
  .project { width: 169px; text-align: center; }
  .project-photo { width: 169px; height: 97px; border: 1px solid #d8cfc2; }
  .project h4 { font-family: "Raleway", sans-serif; font-weight: 400; font-size: 12px; color: var(--white); margin-top: 7px; }
  .project p { font-size: 7.8px; line-height: 1.6; color: #4a3f33; margin-top: 2px; }

  .footer { left: 0; top: 1120px; width: 947px; height: 80px; background: var(--footer); }
  .footer-links { left: 117px; top: 1142px; font-family: "Raleway", sans-serif; font-weight: 500; font-size: 10.5px; color: var(--white); }
  .footer-links span { margin: 0 4px; }
  .footer-copy { left: 117px; top: 1161px; font-size: 7.5px; color: #aaa; }
  .social { left: 766px; top: 1142px; display: flex; gap: 5px; }
  .social span { width: 18px; height: 18px; background: var(--white); border-radius: 3px; }
</style>
</head>
<body>
  <div class="abs brand"><span class="brand-mark"></span>KESTREL PAVING</div>

  <div class="abs quote">
    <div class="quote-label">FREE QUOTE CALL US</div>
    <div class="quote-phone">
      <svg width="14" height="14" viewBox="0 0 24 24" aria-hidden="true"><path fill="#8f7659" d="M6.6 10.8a15.1 15.1 0 0 0 6.6 6.6l2.2-2.2a1 1 0 0 1 1-.25 11.4 11.4 0 0 0 3.6.57 1 1 0 0 1 1 1V20a1 1 0 0 1-1 1A17 17 0 0 1 3 4a1 1 0 0 1 1-1h3.5a1 1 0 0 1 1 1c0 1.25.2 2.45.57 3.57a1 1 0 0 1-.25 1z"/></svg>
      0455210367
    </div>
  </div>

  <nav class="abs nav">
    <a class="active" style="width:92px">HOME</a>
    <a style="width:112px">ABOUT US</a>
    <a style="width:106px">SERVICES</a>
    <a style="width:106px">GALLERY</a>
    <a style="width:112px;border-right:none">CONTACT</a>
  </nav>

  <div class="abs hero" role="img" aria-label="Road roller and paving machine laying fresh asphalt under a cloudy sky"></div>
  <div class="abs hero-caption">
    <div class="hero-kicker">Morbi ornare gravida elit Integer</div>
    <div class="hero-title">Road Construction</div>
    <div class="hero-text">Mauris vel lacus vitae felis vestibulum volutpat Etiam est nunc venenatis in tristique eu imperdiet ac nisl Cum sociis</div>
  </div>
  <div class="abs dots"><span></span><span></span><span></span><span></span></div>

  <section class="abs intro">
    <h1>VIVAMUS PORTTITOR PURUS NISI ELEIFEND</h1>
    <h2>MORBI EGET ARCU MORBI PORTA LIBERO ID ULLAMCORPER</h2>
    <p>Mauris vel lacus vitae felis vestibulum volutpat Etiam est nunc venenatis in tristique eu imperdiet ac nisl Cum sociis natoque penatibus et magnis dis parturient montes nascetur ridiculus mus In iaculis facilisis massa Etiam eu urna Sed porta Suspendisse quam leo molestie sed luctus quis feugiat in pede Fusce tellus Sed metus augue convallis et vehicula ut pulvinar eu ante Integer orci tellus tristique vitae consequat nec porta vel lectus Nulla sit</p>
  </section>

  <article class="abs service" style="left:118px;top:628px">
    <div class="service-photo" role="img" aria-label="Road crew in safety vests cutting asphalt" style="background:linear-gradient(to bottom,#8ea3b8,#9a8c7a 55%,#5e5650)"></div>
    <h3>Road Maintenance</h3>
    <p>Aascetur ridiculus mus In iaculis facilisis massa Etiam eu urna Sed porta Suspendisse quam leo molestie sed luctus quis feugiat in pede Fusce tellus Sed metus</p>
    <span class="btn">READ MORE</span>
  </article>
  <article class="abs service" style="left:363px;top:628px">
    <div class="service-photo" role="img" aria-label="Road roller drums pressing gravel" style="background:linear-gradient(to bottom,#6f6a55,#a08c48 45%,#8a8680)"></div>
    <h3>Road Construction</h3>
    <p>Aascetur ridiculus mus In iaculis facilisis massa Etiam eu urna Sed porta Suspendisse quam leo molestie sed luctus quis feugiat in pede Fusce tellus Sed metus</p>
    <span class="btn">READ MORE</span>
  </article>
  <article class="abs service" style="left:609px;top:628px">
    <div class="service-photo" role="img" aria-label="Grader levelling a new road bed" style="background:linear-gradient(to bottom,#4f82c4,#a9c0d8 40%,#c9c6bf 70%,#b0aca5)"></div>
    <h3>How We Work</h3>
    <p>Aascetur ridiculus mus In iaculis facilisis massa Etiam eu urna Sed porta Suspendisse quam leo molestie sed luctus quis feugiat in pede Fusce tellus Sed metus</p>
    <span class="btn">READ MORE</span>
  </article>

  <section class="abs projects"></section>
  <div class="abs projects-title">RECENT PROJECTS</div>

  <article class="abs project" style="left:118px;top:941px">
    <div class="project-photo" role="img" aria-label="Coastal road winding along the sea" style="background:linear-gradient(to bottom,#7fa6c9,#8a9f86 40%,#6a6a6a 70%,#4a4a4a)"></div>
    <h4>Road Project Name</h4>
    <p>Aascetur ridiculus mus In iaculis facilisis massa Etiam eu urna Sed porta</p>
  </article>
  <article class="abs project" style="left:300px;top:941px">
    <div class="project-photo" role="img" aria-label="Straight road through green fields under blue sky" style="background:linear-gradient(to bottom,#3f78c8,#c7d6e6 35%,#6e9a48 55%,#5a5a5a)"></div>
    <h4>Road Project Name</h4>
    <p>Aascetur ridiculus mus In iaculis facilisis massa Etiam eu urna Sed porta</p>
  </article>
  <article class="abs project" style="left:482px;top:941px">
    <div class="project-photo" role="img" aria-label="Mountain highway curving across a valley" style="background:linear-gradient(to bottom,#3e5f8a,#9aa4a8 35%,#8a7a60 55%,#4c4a48)"></div>
    <h4>Road Project Name</h4>
    <p>Aascetur ridiculus mus In iaculis facilisis massa Etiam eu urna Sed porta</p>
  </article>
  <article class="abs project" style="left:665px;top:941px">
    <div class="project-photo" role="img" aria-label="Open road stretching to a bright horizon" style="background:linear-gradient(to bottom,#5b6a78,#c8c9b8 35%,#6f7a4c 50%,#3e3e3e)"></div>
    <h4>Road Project Name</h4>
    <p>Aascetur ridiculus mus In iaculis facilisis massa Etiam eu urna Sed porta</p>
  </article>

  <footer class="abs footer"></footer>
  <div class="abs footer-links">HOME<span>|</span>ABOUT US<span>|</span>SERVICES<span>|</span>GALLERY<span>|</span>CONTACT</div>
  <div class="abs footer-copy">© 2015 Company Name&nbsp; All right reserved&nbsp; Term of Use</div>
  <div class="abs social" aria-label="Social links"><span></span><span></span><span></span></div>
</body>
</html>
```